Professional Business Cards for Recruiting Company

We'd like professional 2-sided business cards that reflect a color scheme that matches our website, www.quillmerbay.com, and / or logo that is attached.

Slogan used is "We Know People", but needs to be editable because we change it up to "We Know Developers", "We Speak Geek", etc.

Must includes logo, slogan, first and last name, address, email, mobile number and website address.

Files attached for ideas.

Thanks!

Contact Information for Business Card

Logo, Company name, First name, Last name, addresss, email, phone, website address.

Font styles to use
Sans Serif

Colors
0054AA
0677BA
7BADD7
CADEEF
E8F1F8

Requirements
Nice to have
• I do like the following designs. 22962062 and 22962651. Couple ideas anyway.

```html
<!DOCTYPE html>
<html lang="en">
<head>
<meta charset="utf-8">
<title>Quillmer Bay Business Card</title>
<link rel="stylesheet" href="https://fonts.googleapis.com/css2?family=Montserrat:wght@300;400;600;700;800&display=swap">
<style>
  :root {
    --navy: #164a80;
    --brand: #0054aa;
    --sky: #7badd7;
    --mist: #cadeef;
    --haze: #e8f1f8;
    --paper: #ffffff;
    --stage: #ececec;
    --ink: #1c2b4a;
  }
  * { box-sizing: border-box; margin: 0; padding: 0; }
  html, body { width: 1200px; height: 1134px; overflow: hidden; }
  body {
    background: var(--stage);
    font-family: "Montserrat", sans-serif;
    display: flex; flex-direction: column; align-items: center;
    justify-content: space-evenly;
  }
  .card {
    width: 840px; height: 480px; background: var(--paper);
    position: relative; overflow: hidden;
    box-shadow: 0 10px 30px rgba(0,0,0,0.12);
  }

  /* Brand side */
  .brand-side .slogan-area {
    position: absolute; left: 0; top: 0; width: 58%; height: 100%;
  }
  .brand-side .url {
    position: absolute; left: 42px; top: 50%;
    transform: translate(-50%, -50%) rotate(-90deg) translateY(0);
    transform-origin: center;
    font-size: 17px; letter-spacing: 1.5px; color: var(--sky); font-weight: 400;
    white-space: nowrap;
  }
  .brand-side .slogan {
    position: absolute; left: 110px; top: 50%; transform: translateY(-50%);
    font-size: 40px; font-weight: 400; color: var(--navy); letter-spacing: 1px;
  }
  .brand-side .brand-panel {
    position: absolute; right: 0; top: 0; width: 42%; height: 100%;
    background: var(--navy);
    display: flex; flex-direction: column; align-items: center; justify-content: center;
    gap: 22px; color: var(--paper);
  }
  .brand-mark { width: 86px; height: 86px; border: 3px solid var(--paper); }
  .brand-name {
    font-size: 38px; font-weight: 300; letter-spacing: 3px;
    border-bottom: 2px solid var(--paper); padding-bottom: 6px;
  }
  .brand-tagline { font-size: 11px; font-weight: 600; letter-spacing: 1.6px; margin-top: -14px; }

  /* Contact side */
  .contact-side .person {
    position: absolute; left: 200px; top: 44px;
  }
  .person-name { font-size: 34px; color: var(--ink); font-weight: 400; }
  .person-name strong { font-weight: 800; }
  .person-title { font-size: 16px; color: var(--brand); margin-top: 2px; }
  .contact-side .logo-square {
    position: absolute; left: 60px; top: 150px; width: 110px; height: 110px;
    border: 4px solid var(--brand);
  }
  .contact-side .divider {
    position: absolute; left: 230px; top: 140px; width: 2px; height: 290px;
    background: var(--brand);
  }
  .details {
    position: absolute; left: 262px; top: 140px; list-style: none;
    font-size: 16px; line-height: 1.3; color: var(--ink);
  }
  .details li { margin-bottom: 6px; }
  .details .label { display: block; font-weight: 700; color: var(--brand); }
  .details .ext { font-weight: 700; }
  .contact-side .strip {
    position: absolute; right: 0; top: 0; width: 190px; height: 100%;
    background: var(--haze); border-left: 6px solid var(--mist);
    display: flex; align-items: center; justify-content: center;
  }
  .strip-inner {
    transform: rotate(-90deg);
    display: flex; align-items: center; gap: 18px; white-space: nowrap;
  }
  .strip-square { width: 56px; height: 56px; border: 3px solid var(--brand); flex: none; }
  .strip-name {
    font-size: 34px; font-weight: 300; letter-spacing: 2px; color: var(--brand);
    border-bottom: 2px solid var(--brand); line-height: 1.1;
  }
  .strip-tagline { font-size: 9px; font-weight: 600; letter-spacing: 1.2px; color: var(--ink); margin-top: 4px; }
</style>
</head>
<body>

  <section class="card brand-side">
    <div class="slogan-area">
      <span class="url">WWW.QUILLMERBAY.COM</span>
      <p class="slogan">We Know People</p>
    </div>
    <div class="brand-panel">
      <div class="brand-mark"></div>
      <div class="brand-name">QUILLMER BAY</div>
      <div class="brand-tagline">PROFESSIONAL SOURCING AND RECRUITING</div>
    </div>
  </section>

  <section class="card contact-side">
    <div class="person">
      <p class="person-name">Dana <strong>Holloway</strong></p>
      <p class="person-title">President</p>
    </div>
    <div class="logo-square"></div>
    <div class="divider"></div>
    <ul class="details">
      <li><span class="label">Phone</span>555-014-2280 <span class="ext">ext.101</span></li>
      <li><span class="label">Mobile</span>555-019-4417</li>
      <li><span class="label">Email</span>dana.holloway@quillmerbay.com</li>
      <li><span class="label">Website</span>www.quillmerbay.com</li>
      <li><span class="label">Quillmer Bay</span>Millbrook, North Dakota</li>
    </ul>
    <div class="strip">
      <div class="strip-inner">
        <div class="strip-square"></div>
        <div>
          <div class="strip-name">QUILLMER BAY</div>
          <div class="strip-tagline">PROFESSIONAL SOURCING AND RECRUITING</div>
        </div>
      </div>
    </div>
  </section>

</body>
</html>
```